Satchel & Compass needs new business card design

I need a new business card design. I'm looking for out-of-the-box design which represents the freedom of being a location independent entrepreneur.
I offer coaching, retreats and trips.
I would like to see designs with and without the photo.
Colors I use are black (#000000), green (#25A796) and brown (#D7C38C)
Website satchelandcompass.com

Target Market(s)

location independent entrepreneurs, digital nomads, people looking to swap the 9 to 5 for a lifestyle business

Industry/Entity Type

Business

Contact Information for Business Card

Petra Varga
Your Lifestyle Business Coach, Retreat & Trip Leader
http://satchelandcompass.com
hello@satchelandcompass.com
Live a life you don't need a holiday from

Font styles to use
Serif
Sans Serif

Requirements
Must have
• One side should contain only the logo. I would also consider having the "Live a life you don't need a holiday from" on that side too (depending on how it looks)
• Please show both sides on the designs.

```html
<!DOCTYPE html>
<html lang="en">
<head>
<meta charset="utf-8">
<title>Satchel &amp; Compass – Business Card</title>
<link rel="stylesheet" href="https://fonts.googleapis.com/css2?family=Questrial&family=Open+Sans:wght@400&family=Caveat:wght@500&display=swap">
<style>
  :root {
    --backdrop: #d3dadc;
    --card-white: #ffffff;
    --brand-green: #1f9e8c;
    --accent-green: #25a796;
    --ink: #111111;
    --white: #ffffff;
    --foliage-light: #dfe6d6;
    --foliage-mid: #a9b592;
    --foliage-deep: #6f7d5c;
  }
  * { margin: 0; padding: 0; box-sizing: border-box; }
  html, body {
    width: 1181px; height: 1200px; overflow: hidden;
    background: var(--backdrop);
  }
  .canvas { position: relative; width: 1181px; height: 1200px; }

  .card {
    position: absolute; left: 247px; width: 669px;
    border-radius: 22px; overflow: hidden;
  }
  .card--front { top: 90px; height: 410px; background: var(--card-white); }
  .card--back  { top: 665px; height: 395px; background: var(--brand-green); }

  .portrait {
    position: absolute; top: 0; right: 0; width: 400px; height: 100%;
    background:
      linear-gradient(90deg, var(--card-white) 0%, rgba(255,255,255,0) 40%),
      linear-gradient(0deg, var(--card-white) 0%, rgba(255,255,255,0) 30%),
      radial-gradient(ellipse at 60% 40%, var(--foliage-light) 0%, var(--foliage-mid) 55%, var(--foliage-deep) 100%);
  }

  .identity {
    position: absolute; left: 27px; top: 28px;
    border-left: 9px solid var(--accent-green);
    padding-left: 6px; height: 93px;
  }
  .identity__name {
    font-family: "Questrial", sans-serif; font-size: 27px;
    color: var(--ink); line-height: 1; margin-top: 8px;
  }
  .identity__role {
    font-family: "Open Sans", sans-serif; font-size: 16.5px;
    color: var(--accent-green); line-height: 21px; margin-top: 6px;
  }

  .contacts { position: absolute; left: 28px; top: 287px; list-style: none; }
  .contacts li {
    display: flex; align-items: center; height: 31px;
    font-family: "Questrial", sans-serif; font-size: 18px; color: var(--ink);
  }
  .contacts svg { width: 16px; height: 16px; margin-right: 20px; fill: var(--accent-green); }

  .wordmark {
    font-family: "Questrial", sans-serif; color: var(--ink);
    white-space: nowrap; position: absolute;
  }
  .wordmark--front { right: 32px; top: 296px; font-size: 34px; }
  .wordmark--back {
    left: 0; right: 0; top: 128px; text-align: center; font-size: 52px;
  }
  .wordmark__dot {
    display: inline-block; width: 12px; height: 12px; border-radius: 50%;
    background: var(--ink); margin-right: 12px; vertical-align: middle;
  }

  .motto {
    position: absolute; left: 0; right: 0; top: 258px; text-align: center;
    font-family: "Caveat", cursive; font-size: 28px; color: var(--white);
  }
  .motto__emphasis { color: var(--ink); }
</style>
</head>
<body>
<main class="canvas">

  <section class="card card--front">
    <div class="portrait" role="img" aria-label="Photo of the coach outdoors among pine branches holding a small chalkboard sign"></div>

    <header class="identity">
      <h1 class="identity__name">Petra Varga</h1>
      <p class="identity__role">Your Lifestyle Business Coach<br>Retreat &amp; Trip Leader</p>
    </header>

    <ul class="contacts">
      <li>
        <svg viewBox="0 0 16 16" aria-hidden="true"><path d="M1 6c0-2 3-3 7-3s7 1 7 3v1h-4V5.5H5V7H1z M3 8h10l1 5H2z"/></svg>
        0000 000 000
      </li>
      <li>
        <svg viewBox="0 0 16 16" aria-hidden="true"><path d="M1 4h14v9H1z" fill="none" stroke="#25a796" stroke-width="1.4"/><path d="M1 4l7 5 7-5" fill="none" stroke="#25a796" stroke-width="1.4"/></svg>
        hello@satchelandcompass.com
      </li>
      <li>
        <svg viewBox="0 0 16 16" aria-hidden="true" fill="none" stroke="#25a796" stroke-width="1"><circle cx="8" cy="8" r="6.5"/><ellipse cx="8" cy="8" rx="3" ry="6.5"/><path d="M1.5 8h13M2.5 5h11M2.5 11h11"/></svg>
        satchelandcompass.com
      </li>
    </ul>

    <p class="wordmark wordmark--front">Satchel &amp; Compass</p>
  </section>

  <section class="card card--back">
    <p class="wordmark wordmark--back"><span class="wordmark__dot"></span>Satchel &amp; Compass</p>
    <p class="motto">Live a life you don't need a <span class="motto__emphasis">holiday</span> from</p>
  </section>

</main>
</body>
</html>
```